4 Page Music Brochure design

We need assistance in designing a 4 Page A4 (A3 folded) Brochure promoting International Music Tour options for school groups. We have included text in the brief as well as images to be used in the brochure.

```html
<!DOCTYPE html>
<html lang="en">
<head>
<meta charset="utf-8">
<title>Meridian Group Travel – Music Tour Brochure</title>
<link href="https://fonts.googleapis.com/css2?family=Montserrat:wght@600;700;800&family=Open+Sans:wght@400;600;700&display=swap" rel="stylesheet">
<style>
:root{
  --navy:#1d3f7a;
  --blue:#2f6db5;
  --sky:#dce9f7;
  --sky-deep:#b9d2ee;
  --ink:#333a44;
  --grey-box:#e6e8eb;
  --label:#555;
  --white:#ffffff;
}
*{margin:0;padding:0;box-sizing:border-box}
html,body{width:841px;height:1200px;overflow:hidden;background:var(--white)}
body{font-family:"Open Sans",Arial,sans-serif;color:var(--ink)}
.canvas{position:relative;width:841px;height:1200px;background:var(--white)}
.spread-label{position:absolute;font-size:6px;color:var(--label)}
.page{position:absolute;width:420px;overflow:hidden}
.spread-top .page{top:16px;height:580px}
.spread-bottom .page{top:612px;height:584px}
.page-left{left:0}
.page-right{left:421px}

/* Back cover */
.back-cover{background:linear-gradient(180deg,var(--sky) 0%,#eef4fb 100%)}
.back-decor{position:absolute;left:20px;top:40px;width:380px;height:230px;border-radius:50%;
  background:radial-gradient(ellipse at 50% 50%,var(--sky-deep) 0%,rgba(185,210,238,.4) 55%,rgba(220,233,247,0) 72%)}
.back-contact{position:absolute;left:40px;top:300px;font-size:6px;line-height:1.55}
.back-contact strong{display:block;font-size:7px;color:var(--navy)}

/* Front cover */
.front-cover{background:var(--white)}
.cover-photo{position:absolute;left:0;top:0;width:420px;height:234px;
  background:linear-gradient(180deg,#f3b24f 0%,#e47b2c 45%,#5a6f8c 100%)}
.brand{position:absolute;left:0;width:420px;top:252px;text-align:center;
  font-family:"Montserrat",Arial,sans-serif;font-weight:800;color:var(--navy);line-height:1}
.brand .mark{display:inline-block;width:14px;height:14px;border-radius:50%;background:var(--navy);vertical-align:middle;margin-right:8px}
.brand .name-top{font-size:34px;vertical-align:middle}
.brand .name-bottom{display:block;font-size:22px;margin-top:4px;letter-spacing:1px}
.cover-intro{position:absolute;left:30px;top:326px;width:360px;font-size:5.4px;line-height:1.55}
.cover-intro p{margin-bottom:5px}
.itin-title{position:absolute;left:30px;top:414px;font-family:"Montserrat",Arial,sans-serif;font-weight:700;font-size:9px;color:var(--navy)}
.itin-sub{position:absolute;left:30px;top:427px;font-size:5.6px;font-weight:600}
.itin-list{position:absolute;left:30px;top:440px;width:360px;display:grid;grid-template-columns:1fr 1fr;gap:3px 12px;list-style:none;font-size:5.4px}
.itin-list li{background:var(--grey-box);padding:2px 6px;border-left:2px solid var(--blue)}
.itin-list li.plain{background:none;border-left:none;padding-left:0}
.cover-footer{position:absolute;left:0;bottom:0;width:420px;height:50px;background:var(--sky)}

/* Inside pages */
.photo{position:absolute;left:0;width:420px}
.tour-bar{position:absolute;left:0;width:420px;height:12px;background:var(--blue);color:var(--white);
  font-family:"Montserrat",Arial,sans-serif;font-weight:700;font-size:6.4px;line-height:12px;padding-left:10px}
.tour-text{position:absolute;left:10px;width:400px;font-size:5px;line-height:1.5}
</style>
</head>
<body>
<main class="canvas">

  <span class="spread-label" style="left:196px;top:4px">Back Cover</span>
  <span class="spread-label" style="left:610px;top:4px">PAGE 1 (Cover)</span>

  <section class="spread-top">
    <article class="page page-left back-cover">
      <div class="back-decor" role="img" aria-label="Faint aeroplane flying across a globe outline"></div>
      <address class="back-contact">
        <strong>Meridian Group Travel</strong>
        48 Harbour Lane<br>
        Westfield NSW 2190<br>
        (02) 5550 1842<br>
        hello@meridiangroup.example
      </address>
    </article>

    <article class="page page-right front-cover">
      <div class="cover-photo" role="img" aria-label="Passenger jet on the runway at sunset"></div>
      <div class="brand">
        <span class="mark"></span><span class="name-top">MERIDIAN</span>
        <span class="name-bottom">GROUP TRAVEL</span>
      </div>
      <div class="cover-intro">
        <p>Music is best learned where it was written, played and loved by generations of performers.</p>
        <p>We arrange performance tours abroad for school ensembles, choirs and bands so students can share the stage with the world and return inspired.</p>
        <p>Our team handles every detail, from flights and hotels to concert venues, workshops and guided sightseeing, so teachers can focus on the music and on their students while we look after the rest of the journey.</p>
      </div>
      <h2 class="itin-title">Customised Itineraries</h2>
      <p class="itin-sub">Organised travel focused on culture, a performance, events and more</p>
      <ul class="itin-list">
        <li>Concert tours</li><li class="plain">Master classes</li>
        <li>Workshops with musicians</li><li class="plain">Festival and competitions</li>
        <li>School exchanges</li><li class="plain">Sightseeing</li>
        <li>Guided performances</li><li class="plain">Travel insurance and safety</li>
        <li>Instrument rental</li><li class="plain">Group meals and free time</li>
      </ul>
      <div class="cover-footer"></div>
    </article>
  </section>

  <span class="spread-label" style="left:196px;top:601px">Inside PAGE 2</span>
  <span class="spread-label" style="left:610px;top:601px">Inside PAGE 3</span>

  <section class="spread-bottom">
    <article class="page page-left">
      <div class="photo" style="top:0;height:148px;background:linear-gradient(180deg,#8fb3d9 0%,#b49a78 60%,#6e5a44 100%)" role="img" aria-label="Gothic cathedral towers under a blue sky"></div>
      <h3 class="tour-bar" style="top:150px">World Class Choirs in the Heart of Europe</h3>
      <p class="tour-text" style="top:166px">Sing in historic cathedrals and concert halls where choral music has echoed for centuries. Students perform for local audiences, join rehearsals with resident choirs and explore old town squares, museums and markets between concerts on this memorable tour.</p>
      <div class="photo" style="top:204px;height:112px;background:linear-gradient(180deg,#3a1a12 0%,#b8321f 50%,#e07a2a 100%)" role="img" aria-label="Rows of glowing red paper lanterns"></div>
      <h3 class="tour-bar" style="top:318px">Cathedral Hill</h3>
      <p class="tour-text" style="top:334px">This tour blends performance with culture. Groups take part in a shared concert with a host school, attend a traditional music workshop and visit temples, gardens and lively street festivals along the way.</p>
      <div class="photo" style="top:366px;height:100px;background:linear-gradient(180deg,#d9501f 0%,#c2381a 60%,#7a2312 100%)" role="img" aria-label="Long corridor of bright orange shrine gates"></div>
      <h3 class="tour-bar" style="top:468px">Japan Music Tour</h3>
      <p class="tour-text" style="top:484px">Discover a rich musical heritage from ancient drums to modern orchestras. Students perform in schools and community halls, meet young musicians, learn traditional instruments and enjoy city sights, local food and a day of sightseeing by fast train.</p>
    </article>

    <article class="page page-right">
      <div class="photo" style="top:0;height:186px;background:linear-gradient(180deg,#2b1a12 0%,#8a5a2a 45%,#c9963e 75%,#5a2a1a 100%)" role="img" aria-label="Ornate opera house interior with gilded balconies"></div>
      <h3 class="tour-bar" style="top:188px">European Instrumental Tour</h3>
      <p class="tour-text" style="top:204px">Orchestras and bands perform in grand theatres and open air festivals across several countries. The itinerary includes rehearsals with professional conductors, concert attendance, guided tours of composer homes and plenty of time to explore each city with the group.</p>
      <div class="photo" style="top:240px;height:226px;background:linear-gradient(180deg,#d8d2c8 0%,#b3262a 45%,#f1ede6 70%,#9a1e22 100%)" role="img" aria-label="Marching band in red uniforms and tall hats on parade"></div>
      <h3 class="tour-bar" style="top:468px">US Music Tour</h3>
      <p class="tour-text" style="top:484px">March in a famous parade, play at theme park stages and take part in workshops with clinicians from leading music colleges. Groups also visit iconic landmarks, catch a live show and share performances with American school bands on this exciting trip.</p>
    </article>
  </section>

</main>
</body>
</html>
```